Flyer Design

we are cleaning company specialize in home cleaning, based in North Shore in Auckland (NZ).
Company name RW is initial of bright wren.
we provide professional, high standard,attention to detail service,
to make dust-free, sparkling house and no-stress family.

(business practice)--don't write this title
"colour coded cleaning system"
---we use different colour's microfiber cloths and mop heads for more hygene.
"green and clean"
---we use eco-friendly, non-toxic cleaning products for environment and your family's health.

service we offer
regular cleaning service
--weekly, fortnightly, monthly
one-off cleaning service
---move in/out cleaning
---rental inspection cleaning
---spring cleaning
---open home cleaning
---remodeling clean-up
---special occasion cleaning(event,party)

special cleaning
---window cleaning
---oven cleaning
---house washing(water blasting)

Free in home no obligation consultation and 50% off first service.
contact no; Rob and Helen 021 0487 5620,09-561-2047
e-mail info@rwcleaning.example.nz
www.rwcleaning.example.nz

we would like to see designs that use colours blue and lite pink, clean, bright and friendly image.

Target Market(s)

Woman aged between late 30th to 60th, housewives, career woman, senior etc.

Industry/Entity Type

Environment

Requirements
Should not have
• For the introduction instead of writing what I have written above verbatim, would you be able to go to our website and paraphrase/reword the introduction that's already there?

Also please don't use the picture on the website, we are planning to change the picture. Thanks.

```html
<!DOCTYPE html>
<html lang="en">
<head>
<meta charset="utf-8">
<title>RW Cleaning Service Flyer</title>
<link href="https://fonts.googleapis.com/css2?family=Bebas+Neue&family=Oxygen:wght@300;400;700&display=swap" rel="stylesheet">
<style>
:root{
  --page:#eef0f3;
  --pink:#e8b4bc;
  --pink-soft:#f1cdd2;
  --mist:#dbe3ee;
  --white:#ffffff;
  --sky:#7fa3dc;
  --sky-deep:#5f88cc;
  --caption:#a4bae2;
  --navy:#1f5a8e;
  --ink:#3b4656;
  --dot:#e79aa8;
}
*{margin:0;padding:0;box-sizing:border-box}
html,body{width:848px;height:1200px;overflow:hidden;background:var(--page)}
body{position:relative;font-family:"Oxygen",sans-serif;color:var(--ink)}
.flyer{position:absolute;background:var(--white);overflow:hidden;box-shadow:0 2px 8px rgba(0,0,0,.18)}
.flyer--front{left:43px;top:42px;width:763px;height:540px}
.flyer--back{left:41px;top:611px;width:765px;height:539px}
.band{position:absolute;left:0;width:100%}
.band--pink{background:linear-gradient(180deg,var(--pink-soft),var(--pink) 50%,var(--pink-soft))}
.band--mist{background:var(--mist)}
.circle{position:absolute;border-radius:50%;background:var(--white);box-shadow:0 3px 10px rgba(0,0,0,.2)}
.circle__photo{position:absolute;inset:14px;border-radius:50%}
.circle__brand{position:absolute;inset:14px;border-radius:50%;
  background:linear-gradient(160deg,#86a9e0,var(--sky-deep));display:flex;align-items:center;justify-content:center;
  color:var(--white);font-weight:400;white-space:nowrap}
.photo--supplies{background:linear-gradient(135deg,#8d7a6a,#d9c6b4 40%,#6f7fae 75%,#e0a070)}
.photo--collage{background:linear-gradient(135deg,#6d8fcf,#c9b07a 45%,#e8d26a 60%,#b9c6d9)}
.photo--bathroom{background:linear-gradient(140deg,#8f8b86,#dcd8d2 55%,#f4f4f2)}
.photo--bedroom{background:linear-gradient(140deg,#4a3f38,#a08a6a 50%,#e0c44a 70%,#7a6c5e)}
.we-use{position:absolute;font-family:"Bebas Neue",sans-serif;color:var(--caption)}
.we-use__title{left:102px;top:396px;font-size:44px;letter-spacing:1px}
.we-use__text{left:58px;top:458px;font-size:21px;line-height:23px;letter-spacing:.4px;width:700px}
.services{position:absolute;left:56px;top:250px;font-size:13px;line-height:16px}
.services__heading{display:inline-block;background:var(--white);color:var(--navy);font-size:15px;font-weight:400;
  letter-spacing:.5px;padding:0 3px;line-height:18px;margin-bottom:2px}
.services__heading--second{margin-top:10px}
.services ul{list-style:none}
.services li.item::before{content:"";display:inline-block;width:4px;height:4px;border-radius:50%;background:var(--dot);margin-right:2px;vertical-align:middle}
.contact-row{position:absolute;left:250px;top:441px;width:510px;display:flex;justify-content:center;gap:20px}
.contact{font-size:12.5px;color:var(--navy);display:flex;align-items:center;gap:4px;white-space:nowrap}
.contact svg{flex:none}
.contact--phone{position:absolute;left:364px;top:462px}
.contact__names{color:var(--ink);margin-right:6px}
.contact__phone{font-weight:700}
.offer{position:absolute;left:230px;top:479px;width:530px;text-align:center;font-size:13px;font-weight:700;color:var(--navy)}
</style>
</head>
<body>

<section class="flyer flyer--front">
  <div class="band band--pink" style="top:18px;height:170px"></div>
  <div class="band band--mist" style="top:303px;height:215px"></div>

  <div class="circle" style="left:34px;top:68px;width:270px;height:270px">
    <div class="circle__photo photo--supplies" role="img" aria-label="Cleaning spray bottles and folded microfiber cloths in several colours"></div>
  </div>
  <div class="circle" style="left:450px;top:74px;width:254px;height:254px">
    <div class="circle__photo photo--collage" role="img" aria-label="Collage of a tidy bedroom, a gloved hand wiping a surface and window cleaning"></div>
  </div>
  <div class="circle" style="left:234px;top:130px;width:280px;height:280px">
    <div class="circle__brand" style="font-size:23px">R W&nbsp; Cleaning Service</div>
  </div>

  <div class="we-use we-use__title">We use:</div>
  <p class="we-use we-use__text">Different colour's microfiber cloths and mop head or more hygene "green and clean"<br>eco-friendlynon-toxic cleaning for enviroment and your family's health</p>
</section>

<section class="flyer flyer--back">
  <div class="band band--pink" style="top:29px;height:205px"></div>
  <div class="band band--mist" style="top:234px;height:280px"></div>

  <div class="circle" style="left:25px;top:21px;width:184px;height:184px">
    <div class="circle__photo photo--bathroom" role="img" aria-label="Clean modern bathroom with bathtub and vanity"></div>
  </div>
  <div class="circle" style="left:216px;top:84px;width:144px;height:144px">
    <div class="circle__photo photo--bedroom" role="img" aria-label="Neat bedroom with sofa and yellow cushions"></div>
  </div>
  <div class="circle" style="left:347px;top:59px;width:380px;height:380px">
    <div class="circle__brand" style="font-size:31px">R W&nbsp; Cleaning Service</div>
  </div>

  <div class="services">
    <h2 class="services__heading">SERVICE WE OFFER</h2>
    <ul>
      <li>Regular cleaning service</li>
      <li class="item">weekly, fortnightly, monthly</li>
      <li>One-off cleaning service</li>
      <li class="item">move in/out cleaning</li>
      <li class="item">rental inspection cleaning</li>
      <li class="item">spring cleaning</li>
      <li class="item">open home cleaning</li>
      <li class="item">remodeling clean-up</li>
      <li class="item">special occasion cleaning(event,party)</li>
    </ul>
    <h2 class="services__heading services__heading--second">SPECIAL CLEANING</h2>
    <ul>
      <li class="item">window cleaning</li>
      <li class="item">oven cleaning</li>
      <li class="item">house washing(water blasting)</li>
    </ul>
  </div>

  <div class="contact-row">
    <div class="contact contact--email">
      <svg width="18" height="13" viewBox="0 0 18 13" aria-hidden="true"><rect x="1" y="1" width="16" height="11" rx="1" fill="none" stroke="#1f5a8e" stroke-width="1.4"/><path d="M1 1l8 6 8-6" fill="none" stroke="#1f5a8e" stroke-width="1.4"/></svg>
      <span>e-mail info@rwcleaning.example.nz</span>
    </div>
    <div class="contact contact--web">
      <svg width="22" height="16" viewBox="0 0 22 16" aria-hidden="true"><circle cx="8" cy="8" r="6.5" fill="none" stroke="#1f5a8e" stroke-width="1.4"/><path d="M1.5 8h13M8 1.5c-3 3-3 10 0 13M8 1.5c3 3 3 10 0 13" fill="none" stroke="#1f5a8e" stroke-width="1.1"/><path d="M14 12l6 3" stroke="#1f5a8e" stroke-width="2"/></svg>
      <span>www.rwcleaning.example.nz</span>
    </div>
  </div>
  <div class="contact contact--phone">
    <span class="contact__names">Rob and Helen</span>
    <svg width="16" height="16" viewBox="0 0 16 16" aria-hidden="true"><rect x="1" y="1" width="14" height="14" rx="3" fill="none" stroke="#1f5a8e" stroke-width="1.3"/><path d="M5 4c-1 1 0 4 2 6s4 3 5 2l-1.5-1.5-1.2.8c-1-.5-2-1.5-2.5-2.5l.8-1.2z" fill="#1f5a8e"/></svg>
    <span class="contact__phone">021 0487 5620 / 09-561-2047</span>
  </div>
  <p class="offer">Free in home no obligation consultation and 50% off first service.</p>
</section>

</body>
</html>
```